Safety Training company business card design

We are after a high quality, professional business card. We are open to a single or double sided card.

The winning designer must provide the card in a format where we can easily change the name and details of the different people in our organization.

Brindle Guard's company colour is lime green.

We provide all aspects of safety advisory and training for the Building, Civil Construction, Mining, Oil and Gas, Manufacturing, Rail, Rural and Retail sectors.

Visit our website www.brindleguard-example.com.au for training competencies we offer along with our other services including RPL's, safety audits, professional development and client support.

Target Market(s)

Those in the Building, Civil Construction, Mining, Oil and Gas, Manufacturing, Rail, Rural and Retail industries.

Industry/Entity Type

Training

Contact Information for Business Card

Brindle Guard
Safety and Training
Thomas Wellacott
Director
M 0400 555 217
thomas@brindleguard-example.com.au
www.brindleguard-example.com.au
(2 business addresses:)
Penhollow High Risk Training Centre
18 Juniper Parade, Penhollow Q 4000 P 3900 5512 F 3900 5519
Ellerwick Training Centre
67 Talbot Lane, Ellerwick Q 4000 P 4900 2641 F 4900 2648

Colors
9bcb3c

Requirements
Must have
• Lime green must be the main colour. must include BG logo attached, and state Brindle Guard (Safety and Training in smaller/different font).

State something along the lines of:

Nice to have
• We offer remote training and we can come to you.

```html
<!DOCTYPE html>
<html lang="en">
<head>
<meta charset="utf-8">
<title>Brindle Guard – Business Card</title>
<link href="https://fonts.googleapis.com/css2?family=Montserrat:wght@400;500;700;800&display=swap" rel="stylesheet">
<style>
  :root {
    --stage: #1b1b1b;
    --lime: #7fce37;
    --lime-deep: #5fa92b;
    --forest: #2f7d32;
    --forest-dark: #24682a;
    --white: #ffffff;
    --mint-text: #d9f2bf;
    --charcoal: #3a3a3a;
    --charcoal-deep: #262626;
    --grey-text: #b5b5b5;
  }
  * { box-sizing: border-box; margin: 0; padding: 0; }
  html, body {
    width: 1200px; height: 900px; overflow: hidden;
    background: var(--stage);
    font-family: "Montserrat", Arial, sans-serif;
  }
  .stage {
    width: 1200px; height: 900px;
    display: flex; align-items: center; justify-content: center; gap: 40px;
  }
  .card {
    position: relative;
    width: 540px; height: 330px;
    overflow: hidden;
  }

  /* Front */
  .card--front {
    background: linear-gradient(135deg, var(--lime) 0%, #76c433 50%, var(--lime-deep) 100%);
  }
  .brand-mark {
    position: absolute; top: 26px; right: 28px;
    display: flex; align-items: center; gap: 8px;
  }
  .brand-mark__dot {
    width: 12px; height: 12px; border-radius: 50%;
    background: var(--forest);
  }
  .brand-mark__name {
    font-weight: 700; font-size: 14px; color: var(--forest);
    letter-spacing: 0.5px;
  }
  .person {
    position: absolute; left: 36px; top: 92px;
  }
  .person__name {
    font-weight: 800; font-size: 25px; letter-spacing: 1px;
    text-transform: uppercase; color: var(--white);
  }
  .person__surname { color: var(--forest); }
  .person__role {
    margin-top: 10px; font-size: 11px; font-weight: 500;
    letter-spacing: 1px; color: var(--white); text-transform: uppercase;
  }
  .contact-list {
    position: absolute; left: 36px; top: 176px;
    list-style: none;
  }
  .contact-list li {
    display: flex; align-items: center; gap: 10px;
    font-size: 13px; color: var(--white); margin-bottom: 9px;
  }
  .icon { width: 16px; height: 16px; flex: none; }
  .addresses {
    position: absolute; left: 36px; right: 28px; bottom: 26px;
    display: flex; gap: 26px; align-items: flex-end;
  }
  .address {
    font-size: 11px; line-height: 1.45; color: var(--mint-text);
    font-style: normal;
  }
  .address--main { display: flex; gap: 10px; align-items: flex-start; width: 250px; }
  .address--second { width: 220px; }

  /* Back */
  .card--back {
    background: linear-gradient(160deg, var(--charcoal) 0%, var(--charcoal-deep) 100%);
  }
  .website {
    position: absolute; top: 28px; left: 34px;
    font-size: 11px; color: var(--grey-text); letter-spacing: 0.3px;
  }
  .back-brand {
    position: absolute; top: 50%; left: 50%;
    transform: translate(-50%, -50%);
    display: flex; align-items: center; gap: 12px;
  }
  .back-brand__dot {
    width: 20px; height: 20px; border-radius: 50%; background: var(--lime);
  }
  .back-brand__name {
    font-weight: 700; font-size: 30px; color: var(--lime);
  }
  .tagline {
    position: absolute; right: 0; bottom: 70px;
    width: 250px; border-top: 2px solid var(--white);
    padding-top: 8px; padding-right: 26px;
    text-align: right;
    font-size: 11px; font-weight: 500; letter-spacing: 1px;
    color: var(--white); text-transform: uppercase;
  }
</style>
</head>
<body>
<main class="stage">

  <section class="card card--front" aria-label="Business card front">
    <div class="brand-mark">
      <span class="brand-mark__dot"></span>
      <span class="brand-mark__name">Brindle Guard</span>
    </div>

    <div class="person">
      <h1 class="person__name">Thomas <span class="person__surname">Wellacott</span></h1>
      <p class="person__role">Director</p>
    </div>

    <ul class="contact-list">
      <li>
        <svg class="icon" viewBox="0 0 16 16" aria-hidden="true">
          <circle cx="8" cy="8" r="8" fill="var(--forest)"/>
          <path d="M5.2 4.3l1.4-.3.8 1.8-.9.7c.4.9 1.1 1.6 2 2l.7-.9 1.8.8-.3 1.4c-3 .2-5.7-2.5-5.5-5.5z" fill="var(--lime)"/>
        </svg>
        0400 555 217
      </li>
      <li>
        <svg class="icon" viewBox="0 0 16 16" aria-hidden="true">
          <circle cx="8" cy="8" r="8" fill="var(--forest)"/>
          <rect x="4" y="5.2" width="8" height="5.6" rx="0.6" fill="none" stroke="var(--lime)" stroke-width="1"/>
          <path d="M4.3 5.6L8 8.5l3.7-2.9" fill="none" stroke="var(--lime)" stroke-width="1"/>
        </svg>
        thomas@brindleguard-example.com.au
      </li>
    </ul>

    <div class="addresses">
      <address class="address address--main">
        <svg class="icon" viewBox="0 0 16 16" aria-hidden="true">
          <circle cx="8" cy="8" r="8" fill="var(--forest)"/>
          <path d="M8 4l4 3.5h-1.2V11H9V8.8H7V11H5.2V7.5H4z" fill="var(--lime)"/>
        </svg>
        <span>Penhollow High Risk Training Centre 18 Juniper Parade, Penhollow Q 4000 P 3900 5512 F 3900 5519</span>
      </address>
      <address class="address address--second">
        Ellerwick Training Centre<br>
        67 Talbot Lane, Ellerwick Q 4000<br>
        P 4900 2641 F 4900 2648
      </address>
    </div>
  </section>

  <section class="card card--back" aria-label="Business card back">
    <p class="website">www.brindleguard-example.com.au</p>
    <div class="back-brand">
      <span class="back-brand__dot"></span>
      <span class="back-brand__name">Brindle Guard</span>
    </div>
    <p class="tagline">We can come to you</p>
  </section>

</main>
</body>
</html>
```